Stonebrook 720 Real Estate Investment Company

We need a business card designed for a real estate investment company named Stonebrook 720. We want to use red#f04a50, orange #f37122 and yellow #fbee3e as the color scheme. The logo colors will need to be modified from the current blue palette. I've attach VitaPathway logo example that captures the color scheme we're going for for Stonebrook 720. Looking for clean Sans Serif fonts.
Contact Information for Business Card
Daniel Furlow
Managing Partner
48317 Whitfield Lane, Suite 510
Tampa, FL 33718
813-555-4870 Mobile
dfurlow@stonebrook720.example
www.stonebrook720.example
Requirements
Must have
- Looking for creative responses.
Nice to have
- Must hit color palette... orange, red, yellow

```html
<!DOCTYPE html>
<html lang="en">
<head>
<meta charset="utf-8">
<title>Stonebrook 720 – Business Card</title>
<link rel="stylesheet" href="https://fonts.googleapis.com/css2?family=Poppins:wght@300;400;500;700&display=swap">
<style>
  :root {
    --backdrop: #2b2b2b;
    --card: #1f1f1f;
    --edge: #e8262c;
    --red: #f04a50;
    --orange: #f37122;
    --yellow: #fbee3e;
    --ink: #e9e9e9;
    --rule: #8a8a8a;
    --brand: #0c0c0c;
  }
  * { box-sizing: border-box; margin: 0; padding: 0; }
  html, body {
    width: 1200px;
    height: 1200px;
    overflow: hidden;
    background: var(--backdrop);
    font-family: "Poppins", Arial, sans-serif;
  }
  .sheet {
    width: 1200px;
    height: 1200px;
    display: flex;
    flex-direction: column;
    align-items: center;
    justify-content: center;
    gap: 52px;
  }
  .card {
    width: 900px;
    height: 514px;
    background: var(--card);
    border-bottom: 6px solid var(--edge);
    border-radius: 4px;
    box-shadow: 0 18px 40px rgba(0,0,0,.45);
    position: relative;
    display: flex;
    align-items: center;
  }
  .brand {
    display: flex;
    align-items: center;
    gap: 14px;
  }
  .brand-dot {
    width: 22px;
    height: 22px;
    border-radius: 50%;
    background: var(--red);
  }
  .brand-name {
    font-weight: 700;
    color: var(--brand);
    letter-spacing: 0.5px;
    -webkit-text-stroke: 0;
  }

  /* contact side */
  .card--contact .brand-panel {
    width: 52%;
    height: 100%;
    display: flex;
    align-items: center;
    justify-content: center;
  }
  .card--contact .brand-name { font-size: 42px; color: #0a0a0a; }
  .divider {
    width: 1.5px;
    height: 150px;
    background: var(--rule);
  }
  .details {
    padding-left: 40px;
    color: var(--ink);
    font-weight: 300;
    font-size: 19px;
    line-height: 1.55;
  }
  .person-name {
    font-weight: 500;
    font-size: 30px;
    color: var(--red);
    letter-spacing: 0.5px;
    text-transform: uppercase;
    line-height: 1.2;
  }
  .person-title { margin-bottom: 10px; }
  .address { margin-bottom: 12px; }
  .contact-list { list-style: none; }
  .contact-list li {
    display: flex;
    align-items: center;
    gap: 12px;
  }
  .contact-list svg { width: 18px; height: 18px; flex: none; }

  /* logo side */
  .card--logo { justify-content: center; }
  .card--logo .brand-name { font-size: 64px; }
  .card--logo .brand-dot { width: 30px; height: 30px; }
</style>
</head>
<body>
<main class="sheet">

  <section class="card card--contact">
    <div class="brand-panel">
      <div class="brand">
        <span class="brand-name">Stonebrook 720</span>
        <span class="brand-dot"></span>
      </div>
    </div>
    <div class="divider"></div>
    <div class="details">
      <h1 class="person-name">Daniel Furlow</h1>
      <p class="person-title">Managing Partner</p>
      <p class="address">48317 Whitfield Lane<br>Suite 510 Tampa, FL 33718</p>
      <ul class="contact-list">
        <li>
          <svg viewBox="0 0 24 24" aria-hidden="true"><path fill="var(--red)" d="M6.6 10.8a15.1 15.1 0 0 0 6.6 6.6l2.2-2.2a1 1 0 0 1 1-.25 11.4 11.4 0 0 0 3.6.57 1 1 0 0 1 1 1V20a1 1 0 0 1-1 1A17 17 0 0 1 3 4a1 1 0 0 1 1-1h3.5a1 1 0 0 1 1 1c0 1.25.2 2.45.57 3.57a1 1 0 0 1-.25 1z"/></svg>
          813-555-4870
        </li>
        <li>
          <svg viewBox="0 0 24 24" aria-hidden="true"><rect x="3" y="5" width="18" height="14" rx="1.5" fill="none" stroke="var(--orange)" stroke-width="2"/><path d="M3.5 6l8.5 7 8.5-7" fill="none" stroke="var(--orange)" stroke-width="2"/></svg>
          dfurlow@stonebrook720.example
        </li>
        <li>
          <svg viewBox="0 0 24 24" aria-hidden="true"><circle cx="12" cy="12" r="9" fill="none" stroke="var(--yellow)" stroke-width="2"/><path d="M3 12h18M12 3c3 3 3 15 0 18M12 3c-3 3-3 15 0 18" fill="none" stroke="var(--yellow)" stroke-width="1.6"/></svg>
          www.stonebrook720.example
        </li>
      </ul>
    </div>
  </section>

  <section class="card card--logo">
    <div class="brand">
      <span class="brand-name">Stonebrook 720</span>
      <span class="brand-dot"></span>
    </div>
  </section>

</main>
</body>
</html>
```